Popup Banners - BrightCounsel - Legal Technology

- We need two banners (same style) designed with two different images and different text.

- The details of the printing requirements are attached, along with suggested images.

- The banners should share the same theme as our website www.brightcounsel.com.au

- The first banner would include our logo (attached), use the 'roads join' image (attached) in some way and text: New Opportunities - Where legal services and technology meet.

- The second banner would include our logo (attached), use the 'jigsaw' image (attached) in some way and use text: Legal Technology Strategy, Advice and Capability.

- Details on what are required from the Printer is attached also.

Target Market(s)

Legal Professionals

Industry/Entity Type

Information Technology

Font styles to use
Sans Serif

Requirements
Must have
• Our logo (attached), suggested text and the image mentioned for each.
Nice to have
• Professional and modern look
Should not have
• Cheap looking

```html
<!DOCTYPE html>
<html lang="en">
<head>
<meta charset="utf-8">
<title>BrightCounsel – Popup Banners</title>
<link rel="stylesheet" href="https://fonts.googleapis.com/css2?family=Arimo:wght@400;700&family=Bebas+Neue&display=swap">
<style>
  :root {
    --stage: #000000;
    --paper: #ffffff;
    --brand-blue: #5b9fd4;
    --brand-grey: #5a534f;
    --sky-top: #3f7fc4;
    --sky-low: #a9cbe6;
    --grass-light: #7ea64a;
    --grass-dark: #3f6a22;
    --jigsaw-deep: #0f2a44;
    --jigsaw-mid: #2f5e86;
    --jigsaw-glow: #bfe0f4;
  }
  * { margin: 0; padding: 0; box-sizing: border-box; }
  html, body { width: 999px; height: 1200px; overflow: hidden; background: var(--stage); }
  .canvas { position: relative; width: 999px; height: 1200px; background: var(--stage); }

  .banner {
    position: absolute; top: 55px; width: 455px; height: 1123px;
    background: var(--paper); overflow: hidden;
  }
  .banner--roads { left: 33px; }
  .banner--jigsaw { left: 516px; }

  .banner__art { position: absolute; inset: 0; width: 455px; height: 1123px; }

  .brand {
    position: absolute; top: 40px; left: 0; right: 0;
    display: flex; align-items: center; justify-content: center; gap: 18px;
  }
  .brand__mark { width: 30px; height: 30px; background: var(--paper); }
  .brand__name {
    font-family: "Arimo", Arial, sans-serif; font-weight: 700;
    font-size: 33px; letter-spacing: 5px; color: var(--paper);
  }

  .headline {
    position: absolute; left: 0; right: 0; text-align: center;
    font-family: "Bebas Neue", "Oswald", sans-serif; font-weight: 400;
  }
  .headline--blue { top: 642px; font-size: 62px; color: var(--brand-blue); letter-spacing: 0.5px; }
  .headline--grey { top: 680px; font-size: 46px; line-height: 54px; color: var(--brand-grey); letter-spacing: 0.5px; }

  .tagline {
    position: absolute; top: 713px; left: 0; right: 0; text-align: center;
    font-family: "Arimo", Arial, sans-serif; font-weight: 700;
    font-size: 33px; line-height: 47px; color: var(--brand-grey);
  }

  .web {
    position: absolute; top: 948px; left: 0; right: 0; text-align: center;
    font-family: "Arimo", Arial, sans-serif; font-weight: 400;
    font-size: 26px; color: var(--brand-grey);
  }
</style>
</head>
<body>
<main class="canvas">

  <section class="banner banner--roads">
    <svg class="banner__art" viewBox="0 0 455 1123" aria-hidden="false">
      <defs>
        <linearGradient id="roadsPhoto" x1="0" y1="0" x2="0" y2="1">
          <stop offset="0" stop-color="var(--sky-top)"/>
          <stop offset="0.2" stop-color="var(--sky-low)"/>
          <stop offset="0.3" stop-color="var(--grass-light)"/>
          <stop offset="1" stop-color="var(--grass-dark)"/>
        </linearGradient>
      </defs>
      <path class="swoosh-grey" fill="var(--brand-grey)" d="M0,510 C180,512 350,465 455,412 L455,442 C360,500 200,548 0,548 Z"/>
      <path class="swoosh-blue" fill="var(--brand-blue)" d="M120,545 C280,528 400,470 455,398 L455,430 C380,488 270,530 120,545 Z"/>
      <path class="photo" role="img" aria-label="Photo of two dirt roads joining on a grassy hill under a blue sky" fill="url(#roadsPhoto)" d="M0,0 H455 V395 C360,462 200,515 0,518 Z"/>
      <path class="swoosh-blue" fill="var(--brand-blue)" d="M0,932 C90,898 190,884 280,885 C190,893 90,918 0,958 Z"/>
      <path class="swoosh-grey" fill="var(--brand-grey)" d="M0,966 C130,905 310,878 455,900 L455,962 C330,915 150,925 0,975 Z"/>
    </svg>
    <div class="brand"><span class="brand__mark"></span><span class="brand__name">BrightCounsel</span></div>
    <h1 class="headline headline--blue">New Opportunities</h1>
    <p class="tagline">Where legal services<br>and technology meet.</p>
    <p class="web">www.brightcounsel.com.au</p>
  </section>

  <section class="banner banner--jigsaw">
    <svg class="banner__art" viewBox="0 0 455 1123">
      <defs>
        <radialGradient id="jigsawPhoto" cx="0.55" cy="0.45" r="0.7">
          <stop offset="0" stop-color="var(--jigsaw-glow)"/>
          <stop offset="0.45" stop-color="var(--jigsaw-mid)"/>
          <stop offset="1" stop-color="var(--jigsaw-deep)"/>
        </radialGradient>
      </defs>
      <path class="swoosh-grey" fill="var(--brand-grey)" d="M0,510 C180,512 350,465 455,412 L455,442 C360,500 200,548 0,548 Z"/>
      <path class="swoosh-blue" fill="var(--brand-blue)" d="M120,545 C280,528 400,470 455,398 L455,430 C380,488 270,530 120,545 Z"/>
      <path class="photo" role="img" aria-label="Photo of a hand placing a glowing blue jigsaw puzzle piece" fill="url(#jigsawPhoto)" d="M0,0 H455 V395 C360,462 200,515 0,518 Z"/>
      <path class="swoosh-blue" fill="var(--brand-blue)" d="M0,932 C90,898 190,884 280,885 C190,893 90,918 0,958 Z"/>
      <path class="swoosh-grey" fill="var(--brand-grey)" d="M0,966 C130,905 310,878 455,900 L455,962 C330,915 150,925 0,975 Z"/>
    </svg>
    <div class="brand"><span class="brand__mark"></span><span class="brand__name">BrightCounsel</span></div>
    <h1 class="headline headline--grey">Legal Technology Strategy,<br>Advice and Capability</h1>
    <p class="web">www.brightcounsel.com.au</p>
  </section>

</main>
</body>
</html>
```